Summit Glossfloor & Honing
I'm looking for a business card and logo design for my
new Polished Concrete & Grinding business,
If you were to look up Summit in the dictionary it would
say, first in importance, order, or position; leading.
Polished Concrete floors are a niche market, that are being used currently in Shopping centres, office spaces and by most high end architects, builders and designers.
i need my business card & logo to stand out from my
competitors, i need my design + logo to reflect this it
needs to be simple, professional, eye catching, easy
to read and scream quality. The logo will need to be
suitable for a whole range of applications including,
uniforms, letter heads, stickers, and eventually
incorporating in vehicle vinyl wrapping.
Target Market(s)
Builders, architects, Interior designers & home owners
Contact Information for Business Card
Front side:
- Summit Glossfloor & Honing.
- Logo
Rear side:
- Liam Varga
- 0491735082
- info@summitgfh.com.au
- commercial - domestic - industrial
- (later down the line website & space for
social media links
www.summitglossfloor.com.au)
Colors
Designer to choose colors to be used in the design.
Look and feel

```html
<!DOCTYPE html>
<html lang="en">
<head>
<meta charset="utf-8">
<title>Summit Glossfloor &amp; Honing – Business Card</title>
<link rel="stylesheet" href="https://fonts.googleapis.com/css2?family=Montserrat:wght@500;600;700&family=Open+Sans:wght@400&display=swap">
<style>
  :root {
    --stage: #26272a;
    --card-dark: #161617;
    --card-light: #ffffff;
    --slate: #5f7585;
    --slate-light: #8fa3b1;
    --charcoal: #3b3536;
    --ink: #1e1e1e;
    --paper-text: #eeeeee;
  }
  * { margin: 0; padding: 0; box-sizing: border-box; }
  html, body { width: 1200px; height: 900px; overflow: hidden; background: var(--stage); }
  .canvas { position: relative; width: 1200px; height: 900px; }

  .card { position: absolute; left: 300px; width: 600px; height: 340px; overflow: hidden; }
  .card-front { top: 80px; background: var(--card-dark); }
  .card-back { top: 470px; background: var(--card-light); }

  .wordmark { position: absolute; text-align: center; font-family: "Montserrat", sans-serif; }
  .wordmark-name { display: block; font-weight: 600; color: var(--slate-light); letter-spacing: 0.04em; line-height: 1; }
  .wordmark-tagline { display: block; font-weight: 600; text-transform: uppercase; letter-spacing: 0.12em; line-height: 1; }
  .wordmark-mark { display: block; margin: 0 auto; background: var(--slate-light); }

  .card-front .wordmark { left: 0; right: 0; top: 92px; }
  .card-front .wordmark-mark { width: 46px; height: 46px; margin-bottom: 26px; }
  .card-front .wordmark-name { font-size: 58px; }
  .card-front .wordmark-tagline { font-size: 11.5px; color: var(--paper-text); margin-top: 8px; }

  .card-back .wordmark { left: 372px; width: 210px; top: 100px; }
  .card-back .wordmark-mark { width: 30px; height: 30px; margin-bottom: 12px; background: var(--slate); }
  .card-back .wordmark-name { font-size: 34px; color: var(--slate); }
  .card-back .wordmark-tagline { font-size: 7px; color: var(--slate); margin-top: 5px; letter-spacing: 0.08em; }

  .name-tab { position: absolute; left: 0; top: 28px; width: 24px; height: 36px; background: var(--slate); }
  .holder-name { position: absolute; left: 42px; top: 36px; font-family: "Montserrat", sans-serif; font-weight: 700; font-size: 19px; color: var(--slate); letter-spacing: 0.02em; }

  .contact-list { position: absolute; left: 22px; top: 186px; list-style: none; font-family: "Open Sans", sans-serif; font-size: 15.5px; color: var(--ink); }
  .contact-item { display: flex; align-items: center; gap: 10px; height: 24px; }
  .contact-icon { width: 18px; height: 18px; flex: none; }
  .contact-handle-web { position: absolute; left: 84px; top: 264px; font-family: "Open Sans", sans-serif; font-size: 15.5px; color: var(--ink); }

  .bands { position: absolute; left: 0; top: 0; width: 600px; height: 340px; }
  .social { position: absolute; left: 12px; top: 290px; display: flex; align-items: center; gap: 5px; font-family: "Open Sans", sans-serif; font-size: 14px; color: #ffffff; }
  .social-slot { width: 13px; height: 13px; background: #ffffff; border-radius: 2px; }
  .social-handle { margin-left: 8px; }
  .services { position: absolute; left: 290px; top: 302px; width: 300px; text-align: center; font-family: "Montserrat", sans-serif; font-weight: 500; font-size: 14px; letter-spacing: 0.03em; color: var(--paper-text); }
</style>
</head>
<body>
<main class="canvas">

  <section class="card card-front" aria-label="Card front">
    <div class="wordmark">
      <span class="wordmark-mark"></span>
      <span class="wordmark-name">SUMMIT</span>
      <span class="wordmark-tagline">Glossfloor &amp; Honing</span>
    </div>
  </section>

  <section class="card card-back" aria-label="Card back">
    <svg class="bands" viewBox="0 0 600 340" aria-hidden="true">
      <polygon points="0,280 280,280 302,314 0,314" fill="var(--slate)"/>
      <polygon points="280,292 600,292 600,340 310,340" fill="var(--charcoal)"/>
    </svg>

    <div class="name-tab"></div>
    <h1 class="holder-name">LIAM VARGA</h1>

    <div class="wordmark">
      <span class="wordmark-mark"></span>
      <span class="wordmark-name">SUMMIT</span>
      <span class="wordmark-tagline">Glossfloor &amp; Honing</span>
    </div>

    <ul class="contact-list">
      <li class="contact-item">
        <svg class="contact-icon" viewBox="0 0 18 18"><circle cx="9" cy="9" r="8" fill="none" stroke="#555" stroke-width="1.2"/><path d="M6.3 5.2l1.4-.4 1 2-1 .8c.4 1 1.2 1.8 2.2 2.3l.8-1 2 1-.4 1.4c-3 .2-6.2-3-6-6.1z" fill="#555"/></svg>
        <span>0491735082</span>
      </li>
      <li class="contact-item">
        <svg class="contact-icon" viewBox="0 0 18 18"><circle cx="9" cy="9" r="8" fill="none" stroke="#555" stroke-width="1.2"/><rect x="5" y="6" width="8" height="6" fill="#555"/><path d="M5 6l4 3.2L13 6" fill="none" stroke="#fff" stroke-width="0.9"/></svg>
        <span>info@summitgfh.com.au</span>
      </li>
      <li class="contact-item">
        <svg class="contact-icon" viewBox="0 0 18 18"><circle cx="9" cy="9" r="8" fill="none" stroke="#555" stroke-width="1.2"/><circle cx="9" cy="9" r="4.5" fill="none" stroke="#777" stroke-width="0.9"/><path d="M4.5 9h9M9 4.5v9" stroke="#777" stroke-width="0.9"/></svg>
        <span>www.summitglossfloor.com.au</span>
      </li>
    </ul>
    <p class="contact-handle-web">/summitglossfloor.com.au</p>

    <div class="social">
      <span class="social-slot"></span>
      <span class="social-slot"></span>
      <span class="social-slot"></span>
      <span class="social-handle">/summitglossfloor</span>
    </div>

    <p class="services">COMMERCIAL - DOMESTIC - INDUSTRIAL</p>
  </section>

</main>
</body>
</html>
```